BRD business cards Dr. Martin Velk

I need a business card designed for our dental office. We are a "general dental" practice.
Looking for a clean, professional but not too fancy design with our logo and contact information required.
front of card is information/standard business card, backside is appt reminder with lines for date and time of appt
doctors name: Dr. Martin Velk DMD
office name: Velk Family Dental
address: 4827 E Tolland Ave Brindle Park, FL 33991
phone: 954-555-0173
Dentistry
Office name, Doctor name, address, phone number...etc
- White/off white base color, blue and or black lettering

```html
<!DOCTYPE html>
<html lang="en">
<head>
<meta charset="utf-8">
<title>Velk Family Dental – Business Card</title>
<link href="https://fonts.googleapis.com/css2?family=Crimson+Text:wght@400;700&display=swap" rel="stylesheet">
<style>
  :root {
    --page-bg: #e4e3e2;
    --card-front: #ececec;
    --card-back: #f7f7f7;
    --ink: #141414;
    --ink-soft: #2a2a2a;
    --rule: #3a3a3a;
  }
  * { box-sizing: border-box; margin: 0; padding: 0; }
  html, body {
    width: 1200px; height: 1200px; overflow: hidden;
    background: var(--page-bg);
    font-family: "Crimson Text", Georgia, serif;
    color: var(--ink);
  }
  .card {
    position: absolute;
    left: 242px;
    width: 703px;
    height: 400px;
  }
  .card--front { top: 170px; background: var(--card-front); }
  .card--back  { top: 629px; background: var(--card-back); }

  .brand {
    position: absolute;
    left: 66px; top: 226px;
    display: flex; align-items: center; gap: 12px;
    font-size: 27px; font-weight: 400;
    letter-spacing: 1px; text-transform: uppercase;
    color: var(--ink);
  }
  .brand__dot {
    width: 14px; height: 14px; border-radius: 50%;
    background: var(--ink);
  }

  .doctor {
    position: absolute; right: 24px; top: 22px;
    text-align: right; line-height: 1.1;
  }
  .doctor__name { font-size: 27px; font-weight: 700; letter-spacing: 0.3px; }
  .doctor__title { font-size: 22px; font-weight: 400; }

  .contact {
    position: absolute; right: 24px; top: 264px;
    text-align: right; font-size: 20px; line-height: 27px;
    color: var(--ink-soft);
  }
  .contact__phone { margin-top: 16px; }

  .appt__heading {
    position: absolute; top: 86px; left: 0; right: 0;
    text-align: center; font-size: 21px; color: var(--ink-soft);
  }
  .appt__row {
    position: absolute; left: 104px;
    display: flex; align-items: flex-end;
    font-size: 18px; color: var(--ink-soft);
  }
  .appt__row--date { top: 196px; }
  .appt__row--time { top: 260px; }
  .appt__label { width: 53px; }
  .appt__colon { width: 23px; }
  .appt__line {
    width: 363px; height: 1px; background: var(--rule);
    margin-bottom: 4px;
  }
</style>
</head>
<body>
  <section class="card card--front" aria-label="Business card front">
    <div class="brand"><span class="brand__dot"></span>Velk Family Dental</div>
    <div class="doctor">
      <div class="doctor__name">DR. MARTIN VELK</div>
      <div class="doctor__title">DMD</div>
    </div>
    <div class="contact">
      <div>4827 E Tolland Ave</div>
      <div>Brindle Park, FL 33991</div>
      <div class="contact__phone">954-555-0173</div>
    </div>
  </section>

  <section class="card card--back" aria-label="Appointment reminder">
    <div class="appt__heading">Next Appointment</div>
    <div class="appt__row appt__row--date">
      <span class="appt__label">ON</span><span class="appt__colon">:</span><span class="appt__line"></span>
    </div>
    <div class="appt__row appt__row--time">
      <span class="appt__label">AT</span><span class="appt__colon">:</span><span class="appt__line"></span>
    </div>
  </section>
</body>
</html>
```